High-end residential home builder needs a business card design

We need a new business card design for a small residential construction company based in Boise, Idaho. We specialize in building custom high-end homes and remodels, with a focus on great design and craftsmanship.

We would like to use our current logo, but open to new color suggestions.
Just looking for a clean, sharp, modern design that looks high-end.

Target Market(s)

Upscale clientele

Industry/Entity Type

Contractor

Contact Information for Business Card

Company: Stonefield Custom Builders
Name: Marcus Tilley
Phone number: 208 367 4120
Email: MarcusTilleySCB@mailbox-example.com
Website: Stonefieldcustombuilders-example.com

Font styles to use
Serif
Sans Serif

Requirements
Must have
• Company Logo
Company name
My name
My phone number
My email
Company website
Nice to have
• I have attached a few photos of cards that I really like.

```html
<!DOCTYPE html>
<html lang="en">
<head>
<meta charset="utf-8">
<title>Stonefield Custom Builders – Business Card</title>
<link rel="stylesheet" href="https://fonts.googleapis.com/css2?family=Michroma&family=Raleway:wght@400;500&display=swap">
<style>
  :root {
    --backdrop: #cdb48e;
    --card: #ece9e3;
    --ink-brown: #2a1a12;
    --accent-orange: #e08a1e;
    --ink-navy: #1f2a5c;
    --ink-text: #222222;
    --card-shadow: rgba(60, 40, 20, 0.28);
  }
  * { box-sizing: border-box; margin: 0; padding: 0; }
  html, body {
    width: 1200px;
    height: 857px;
    overflow: hidden;
  }
  body {
    position: relative;
    background: var(--backdrop);
    font-family: "Raleway", sans-serif;
  }
  .card {
    position: absolute;
    left: 335px;
    width: 540px;
    height: 310px;
    background: var(--card);
    box-shadow: 0 10px 22px var(--card-shadow);
  }
  .card--front { top: 79px; }
  .card--back { top: 467px; }

  /* Front */
  .brand-block {
    position: absolute;
    left: 0;
    right: 0;
    top: 96px;
    text-align: center;
    color: var(--ink-brown);
  }
  .brand-block__square {
    display: block;
    width: 44px;
    height: 44px;
    margin: 0 auto 38px;
    border: 3px solid var(--ink-brown);
  }
  .brand-block__name {
    font-family: "Raleway", sans-serif;
    font-weight: 500;
    font-size: 19px;
    letter-spacing: 0.42em;
    padding-left: 0.42em;
    line-height: 1;
  }
  .brand-block__sub {
    margin-top: 14px;
    font-family: "Raleway", sans-serif;
    font-weight: 500;
    font-size: 10px;
    letter-spacing: 0.42em;
    padding-left: 0.42em;
    line-height: 1;
  }

  /* Back */
  .brand-side {
    position: absolute;
    left: 38px;
    top: 98px;
    width: 128px;
    text-align: center;
    color: var(--ink-brown);
  }
  .brand-side__square {
    display: block;
    width: 56px;
    height: 56px;
    margin: 0 auto 16px;
    border: 3px solid var(--ink-brown);
  }
  .brand-side__name {
    font-family: "Raleway", sans-serif;
    font-weight: 500;
    font-size: 11px;
    letter-spacing: 0.3em;
    padding-left: 0.3em;
  }
  .person {
    position: absolute;
    right: 46px;
    top: 38px;
    text-align: right;
    color: var(--ink-navy);
  }
  .person__name {
    font-family: "Michroma", sans-serif;
    font-size: 16px;
    font-weight: 400;
    letter-spacing: 0.08em;
    line-height: 1.2;
    -webkit-text-stroke: 0.6px var(--ink-navy);
  }
  .person__role {
    margin-top: 10px;
    font-size: 12px;
    font-weight: 500;
    letter-spacing: 0.08em;
  }
  .contact {
    position: absolute;
    right: 46px;
    top: 199px;
    list-style: none;
    text-align: right;
    color: var(--ink-text);
    font-size: 11.5px;
    letter-spacing: 0.04em;
    line-height: 18.7px;
  }
  .contact__label { margin-right: 8px; }
</style>
</head>
<body>
  <section class="card card--front" aria-label="Business card front">
    <div class="brand-block">
      <span class="brand-block__square" aria-hidden="true"></span>
      <p class="brand-block__name">STONEFIELD</p>
      <p class="brand-block__sub">CUSTOM BUILDERS</p>
    </div>
  </section>

  <section class="card card--back" aria-label="Business card back">
    <div class="brand-side">
      <span class="brand-side__square" aria-hidden="true"></span>
      <p class="brand-side__name">STONEFIELD</p>
    </div>
    <div class="person">
      <h1 class="person__name">MARCUS TILLEY</h1>
      <p class="person__role">DIRECTOR</p>
    </div>
    <ul class="contact">
      <li><span class="contact__label">Phone:</span> +0208 367 4120</li>
      <li><span class="contact__label">Mail:</span> MarcusTilleySCB@mailbox-example.com</li>
      <li>www.stonefieldcustombuilders-example.com</li>
      <li>123 , Street, City, World, Name , 23545</li>
    </ul>
  </section>
</body>
</html>
```